Website for a new t-shirt company called wrendusktees.com

We are looking for a talented web designer to create a website that aligns with our brand's message and identity centered around the theme of "Wren Dusk." The website should be modern, clean, and visually appealing while also being user-friendly and easy to navigate.

We will be using the Big Commerce platform for our online store section, so the designer should have experience in designing websites on this platform.

We would like the website to have the following elements:

A color scheme that aligns with the brand's identity and message
A homepage that showcases our products and message, with clear calls-to-action for visitors to explore further
A blog section that highlights our brand's philosophy and offers advice and tips for people looking to make positive changes in their lives
An "About Us" section that introduces our brand and team and offers insight into our mission and values
A contact form that allows visitors to easily get in touch with us for inquiries or support
We are open to creative suggestions and ideas from the designer, but we would like the website to have a modern and minimalist aesthetic that resonates with our target audience of 20 to 40-year-olds.

```html
<!DOCTYPE html>
<html lang="en">
<head>
<meta charset="utf-8">
<title>Wren Dusk — T-Shirts</title>
<link href="https://fonts.googleapis.com/css2?family=Montserrat:wght@400;500;600;700&family=Pathway+Gothic+One&family=Bebas+Neue&display=swap" rel="stylesheet">
<style>
:root{
  --ink:#161616;
  --panel:#1d1d1d;
  --muted:#555;
  --line:#cfcfcf;
  --bar:#e3e3e5;
  --white:#fff;
  --hero-a:#f4f4f4;
  --hero-b:#cfcfcf;
}
*{box-sizing:border-box;margin:0;padding:0}
html,body{width:1200px;height:4451px;overflow:hidden}
body{position:relative;background:var(--white);font-family:"Montserrat",sans-serif;color:var(--ink)}
.abs{position:absolute}
.title{font-family:"Pathway Gothic One",sans-serif;font-size:40px;font-weight:400;text-align:center;width:1200px;left:0}
.btn{display:flex;align-items:center;justify-content:center;background:var(--ink);color:var(--white);font-size:16px;font-weight:500}
.btn--light{background:var(--white);color:var(--ink)}
.brand{font-family:"Montserrat",sans-serif;font-weight:600;color:var(--ink);white-space:nowrap}

.topbar{top:0;left:0;width:1200px;height:55px;background:var(--bar);font-size:12px;display:flex;justify-content:space-between;align-items:center;padding:0 112px}
.header{top:55px;left:0;width:1200px;height:101px;border-bottom:1px solid var(--line)}
.header .brand{position:absolute;left:0;width:1200px;text-align:center;top:34px;font-size:32px}
.icons-left{position:absolute;left:112px;top:38px;display:flex;gap:14px}
.icons-right{position:absolute;right:120px;top:42px;display:flex;gap:22px;align-items:center;font-family:"Bebas Neue",sans-serif;font-size:18px}
.badge{position:relative}
.badge span{position:absolute;right:-6px;top:-8px;width:14px;height:14px;border-radius:50%;background:var(--ink);color:#fff;font:600 8px "Montserrat",sans-serif;display:flex;align-items:center;justify-content:center;border:1px solid #fff}
.nav{top:156px;left:0;width:1200px;height:46px;display:flex;justify-content:center;align-items:center;gap:52px;font-size:14px;border-bottom:1px solid var(--line)}

.hero{top:203px;left:0;width:1200px;height:584px;background:radial-gradient(ellipse at 50% 40%,var(--hero-a),var(--hero-b))}
.hero-photo{position:absolute;left:740px;top:15px;width:230px;height:560px;background:linear-gradient(180deg,#e8e8e8,#d6d6d6 60%,#c9c9c9);border-radius:6px}
.hero-text{position:absolute;left:0;width:1200px;text-align:center}
.hero h2{font-family:"Bebas Neue",sans-serif;font-weight:400;font-size:44px;top:178px}
.hero h1{font-family:"Bebas Neue",sans-serif;font-weight:400;font-size:92px;top:222px;line-height:1}
.hero p{top:320px;font-size:16px;line-height:29px;color:#333}
.hero .btn{left:522px;top:403px;width:155px;height:42px}
.arrow{position:absolute}

.card{top:956px;width:213px;height:370px;border:1.5px solid #555;background:var(--white);text-align:center}
.card .img{margin:14px auto 0;width:178px;height:160px;background:linear-gradient(#eeeeee,#dcdcdc)}
.stars{font-size:19px;letter-spacing:1px;margin-top:10px}
.card .name{font-size:16px;line-height:29px;color:#333;margin-top:6px;padding:0 24px}
.card .price{font-size:18px;font-weight:700}
.card--active{background:#f3f3f3}
.card--active .img{height:140px;background:var(--white);border-bottom:1px solid var(--line);margin-top:0;width:100%;display:flex;align-items:center;justify-content:center}
.card--active .btn{margin:10px auto 0;width:155px;height:40px}

.about-photo{top:1620px;left:66px;width:534px;height:398px;background:linear-gradient(135deg,#6b7780,#9c8d86 50%,#c7c8cc)}
.about-box{top:1651px;left:600px;width:486px;height:337px;border:2px solid #444;border-left:none;padding:22px 24px 0 20px}
.about-box h3{font-size:16px;font-weight:700}
.about-box p{margin-top:18px;font-size:16px;line-height:29px;color:#444;text-align:justify;height:174px;overflow:hidden}
.about-box .btn{margin-top:18px;width:155px;height:40px}

.blog-panel{top:2212px;left:112px;width:903px;height:399px;background:linear-gradient(120deg,#4e4f53,#37383c 60%,#1e2a3a)}
.blog-photo{top:2250px;left:595px;width:494px;height:302px;background:linear-gradient(110deg,#bfc0c2,#77797d 45%,#2a6fa3 70%,#b9bbbd)}
.blog-text{top:2262px;left:158px;width:405px;color:var(--white)}
.blog-text h3{font-family:"Pathway Gothic One",sans-serif;font-weight:400;font-size:30px}
.blog-text p{margin-top:22px;font-size:16px;line-height:29px}
.blog-text .btn{margin-top:30px;width:155px;height:42px}

.team-intro{top:2878px;left:0;width:1200px;text-align:center;font-size:16px;line-height:29px;color:#333}
.member{top:2981px;width:240px;height:310px}
.member--hover{display:flex;flex-direction:column;justify-content:center;align-items:center;color:#fff;text-align:center;padding:0 40px}
.member--hover h4{font-size:17px;font-weight:700}
.member--hover p{font-size:16px;line-height:25px;margin-top:10px}

.contact{top:3401px;left:112px;width:976px;height:419px;background:var(--panel);color:#fff}
.contact h3{position:absolute;left:57px;top:52px;font-family:"Pathway Gothic One",sans-serif;font-weight:400;font-size:40px}
.contact p{position:absolute;left:57px;top:140px;width:370px;font-size:16px;line-height:29px}
.social{display:flex;gap:14px}
.social i{width:24px;height:24px;border-radius:50%;background:#6d6d6d;display:block}
.contact .social{position:absolute;left:57px;top:248px}
.field{position:absolute;left:547px;width:354px;height:56px;border:1.5px solid #9a9a9a;font-size:16px;color:#aaa;padding:18px 16px}
.contact .btn{position:absolute;left:645px;top:302px;width:155px;height:40px}

.f-line{top:3960px;height:3px;background:var(--ink)}
.footer .brand{top:3938px;left:0;width:1200px;text-align:center;font-size:38px}
.f-nav{top:4058px;left:0;width:1200px;display:flex;justify-content:center;gap:60px;font-size:16px}
.f-links{top:4148px;left:100px;width:196px;text-align:center;font-size:16px;line-height:29px}
.footer .social{position:absolute;left:548px;top:4138px}
.f-sign{top:4212px;left:0;width:1200px;text-align:center;font-size:16px;line-height:29px}
.f-email{top:4290px;left:439px;width:315px;height:46px;border:1.5px solid var(--ink);font-size:16px;padding:12px 14px;display:flex;justify-content:space-between;align-items:center}
.f-addr{top:4136px;right:111px;text-align:right;font-size:16px;line-height:29px}
.copy{top:4382px;left:0;width:1200px;height:69px;background:var(--bar);display:flex;align-items:center;justify-content:center;font-size:14px}
</style>
</head>
<body>

<div class="abs topbar"><span>FREE SHIPPING ON ORDERS OVER $75</span><span>PHONE: 555 014 2270</span></div>

<header class="abs header">
  <div class="icons-left">
    <svg width="20" height="22" viewBox="0 0 20 22"><circle cx="10" cy="6" r="5" fill="#161616"/><path d="M1 21c0-6 4-9 9-9s9 3 9 9z" fill="#161616"/></svg>
    <svg width="22" height="22" viewBox="0 0 22 22"><circle cx="9" cy="9" r="7" fill="none" stroke="#161616" stroke-width="2.5"/><path d="M14 14l6 6" stroke="#161616" stroke-width="2.5"/></svg>
  </div>
  <div class="brand">Wren Dusk</div>
  <div class="icons-right">
    <span>US Dollar $ ⌄</span>
    <span class="badge"><svg width="24" height="22" viewBox="0 0 24 22"><path d="M12 21L2 11C-1 7 2 1 7 2c2 0 4 2 5 3 1-1 3-3 5-3 5-1 8 5 5 9z" fill="#161616"/></svg><span>3</span></span>
    <span class="badge"><svg width="26" height="24" viewBox="0 0 26 24"><path d="M1 2h4l3 13h13l3-9H7" fill="#161616" stroke="#161616" stroke-width="2"/><circle cx="10" cy="20" r="2.5" fill="#161616"/><circle cx="19" cy="20" r="2.5" fill="#161616"/></svg><span>3</span></span>
  </div>
</header>

<nav class="abs nav"><span>HOME</span><span>ABOUT US</span><span>MISSION &amp; VALUES</span><span>BLOG</span><span>TEAM</span><span>CONTACT</span></nav>

<section class="abs hero">
  <div class="hero-photo" role="img" aria-label="Model in a white t-shirt and shorts seated on a white cube"></div>
  <h2 class="hero-text">WELCOME TO</h2>
  <h1 class="hero-text">WREN DUSK</h1>
  <p class="hero-text">Lorem ipsum dolor sit amet, consectetur adipiscing elit, sed do<br>eiusmod ut labore et dolore magna aliqua.</p>
  <div class="abs btn">Shop Now</div>
  <svg class="arrow" style="left:36px;top:270px" width="20" height="30" viewBox="0 0 20 30"><path d="M16 3L4 15l12 12" fill="none" stroke="#161616" stroke-width="3"/></svg>
  <svg class="arrow" style="left:1144px;top:270px" width="20" height="30" viewBox="0 0 20 30"><path d="M4 3l12 12L4 27" fill="none" stroke="#161616" stroke-width="3"/></svg>
</section>

<h2 class="abs title" style="top:860px">Products</h2>
<svg class="arrow" style="left:36px;top:1130px" width="18" height="28" viewBox="0 0 18 28"><path d="M15 3L4 14l11 11" fill="none" stroke="#161616" stroke-width="3"/></svg>
<svg class="arrow" style="left:1146px;top:1130px" width="18" height="28" viewBox="0 0 18 28"><path d="M3 3l11 11L3 25" fill="none" stroke="#161616" stroke-width="3"/></svg>

<div class="abs card" style="left:40px"><div class="img" role="img" aria-label="Model wearing a grey knit sweater"></div><div class="stars">★★★★★</div><div class="name">Tshirt With Round Neck</div><div class="price">$25.99</div></div>
<div class="abs card" style="left:266px"><div class="img" role="img" aria-label="Model wearing a red sweatshirt"></div><div class="stars">★★★★★</div><div class="name">Tshirt With Round Neck</div><div class="price">$25.99</div></div>
<div class="abs card card--active" style="left:491px"><div class="img" role="img" aria-label="Black round neck t-shirt"><svg width="110" height="100" viewBox="0 0 110 100"><path d="M38 6l-30 16 12 22 12-6v58h46V38l12 6 12-22-30-16c-4 8-12 10-17 10s-13-2-17-10z" fill="#111"/></svg></div><div class="stars">★★★★★</div><div class="name">Tshirt With Round Neck</div><div class="price">$25.99</div><div class="btn">Shop Now</div></div>
<div class="abs card" style="left:716px"><div class="img" role="img" aria-label="Model wearing a light blue t-shirt"></div><div class="stars">★★★★★</div><div class="name">Tshirt With Round Neck</div><div class="price">$25.99</div></div>
<div class="abs card" style="left:941px"><div class="img" role="img" aria-label="Model wearing a blue t-shirt holding a phone"></div><div class="stars">★★★★★</div><div class="name">Tshirt With Round Neck</div><div class="price">$25.99</div></div>

<div class="abs btn" style="left:522px;top:1380px;width:155px;height:41px">View More</div>

<h2 class="abs title" style="top:1520px">About Us</h2>
<div class="abs about-photo" role="img" aria-label="Team collaborating around a table in an office"></div>
<div class="abs about-box">
  <h3>Mission &amp; Values</h3>
  <p>Lorem ipsum dolor sit amet, consectetur adipiscing elit, sed do eiusmod tempor incididunt ut labore et dolore magna aliqua. Quis ipsum suspendisse ultrices gravida. Risus commodo viverra maecenas accumsan lacus vel facilisis. Lorem ipsum dolor sit amet, consectetur adipiscing elit, sed do eiusmod tempor incididunt ut</p>
  <div class="btn">Read More</div>
</div>

<h2 class="abs title" style="top:2116px">Blog</h2>
<div class="abs blog-panel" role="img" aria-label="Faded fashion photo background"></div>
<div class="abs blog-photo" role="img" aria-label="Model in a blue outfit lying on a staircase"></div>
<div class="abs blog-text">
  <h3>Wren Dusk Blog Sample</h3>
  <p>Lorem ipsum dolor sit amet, consectetur adipiscing elit, sed do eiusmod tempor incididunt ut labore et dolore magna aliqua. Quis ipsum suspendisse ultrices gravida. Risus commodo viverra maecenas accumsan lacus vel facilisis.</p>
  <div class="btn btn--light">Read More</div>
</div>
<div class="abs btn" style="left:522px;top:2656px;width:155px;height:41px">View&nbsp; More</div>

<h2 class="abs title" style="top:2798px">Team</h2>
<p class="abs team-intro">Lorem ipsum dolor sit amet, consectetur adipiscing elit, sed do eiusmod tempor incididunt ut labore et dolore magna aliqua.<br>Quis ipsum suspendisse ultrices gravida. Risus commodo viverra maecenas accumsan lacus vel facilisis.</p>
<div class="abs member" style="left:0;background:linear-gradient(#f2f2f2,#3a3a3a)" role="img" aria-label="Team member portrait in a suit"></div>
<div class="abs member" style="left:240px;background:linear-gradient(#7a6a58,#8e949a)" role="img" aria-label="Team member portrait in a grey shirt"></div>
<div class="abs member member--hover" style="left:480px;background:linear-gradient(#3b3d42,#222)" role="img" aria-label="Team member portrait, darkened with caption">
  <h4>Sam Rivera</h4>
  <p>Lorem ipsum dolor sit amet, consectetur adipiscing elit, sed do eiusmod tempor incididunt ut labore.</p>
</div>
<div class="abs member" style="left:720px;background:linear-gradient(#ffffff,#e4e4e4)" role="img" aria-label="Team member portrait in a white polo"></div>
<div class="abs member" style="left:960px;background:linear-gradient(#f4f4f4,#c9b172)" role="img" aria-label="Team member portrait in a yellow jacket"></div>

<section class="abs contact">
  <h3>Contact Us</h3>
  <p>Lorem ipsum dolor sit amet, consectetur adipiscing elit, sed do eiusmod tempor incididunt ut labore et dolore magna aliqua.</p>
  <div class="social"><i></i><i></i><i></i></div>
  <div class="field" style="top:73px">Name</div>
  <div class="field" style="top:145px">Email</div>
  <div class="field" style="top:217px">Phone</div>
  <div class="btn btn--light">Get In Touch</div>
</section>

<footer class="footer">
  <div class="abs f-line" style="left:0;width:450px"></div>
  <div class="abs f-line" style="left:744px;width:456px"></div>
  <div class="abs brand">Wren Dusk</div>
  <div class="abs f-nav"><span>HOME</span><span>ABOUT US</span><span>MISSION &amp; VALUES</span><span>BLOG</span><span>TEAM</span><span>CONTACT</span></div>
  <div class="abs f-links">PRIVACY POLICY<br>TERMS &amp; CONDITIONS<br>SUPPORT</div>
  <div class="social"><i></i><i></i><i></i></div>
  <div class="abs f-sign">SIGN UP FOR THE LATEST NEWS AND<br>OFFERS</div>
  <div class="abs f-email"><span>Email</span><svg width="26" height="20" viewBox="0 0 26 20"><path d="M1 1l24 9-24 9 5-9z" fill="#161616"/></svg></div>
  <div class="abs f-addr">#12, Linden Lane, Ashford,<br>USA - 402117<br>(+1) 555 014 2270<br>info@wrendusktees.com</div>
  <div class="abs copy">© Copyrights 2023 Wren Dusk | All Rights Reserved</div>
</footer>

</body>
</html>
```